We operate a niche online Job Board in Australia. The website is called 'Harbourline Careers Australia' and is used by Christian Employers to advertise their job vacancies.
I would like a business card that identifies with our website (www.harbourlinecareers.com.au). We would like the same colors and fonts used on our business card from our website. When people look at our business card we want them to be able to recognise it from the website.
We want the web address to be dominant.
Updates
We are liking those that use white space as well as the blue and orange and those that highlight the url.
We now have 60 designs and therefore will not wait for the Sunday deadline to make a decision. We have a few we like.
The ones we like are:
- bold
- creative
- colorful (blue orange and white)
- some white space
- no boxes or borders
- font the same as our website
- reflects the look of our website
We will make a final decision in the next 6 hours so please if you think you have something to offer then get it in within the next 6 hours. If you think you will leave it till later you will miss out. Thanks to all those who have responded with some great designs, sorry we can't reward all of you!
Industry/Entity Type
Business
Contact Information for Business Card
Harbourline Careers Australia
www.harbourlinecareers.com.au
Gregory Palliser
CEO
Phone: 1300 574 816
Mobile: 0412 937215
Fax: (03) 9172 4463
email: gregory@harbourlinecareers.com.au
Requirements
Should not have
- We do not want a cross or any cliche christian images.

```html
<!DOCTYPE html>
<html lang="en">
<head>
<meta charset="utf-8">
<title>Harbourline Careers Australia – Business Card</title>
<link rel="stylesheet" href="https://fonts.googleapis.com/css2?family=Noto+Serif&family=Arimo:wght@400&family=Tinos&display=swap">
<style>
  :root {
    --navy: #0b0f5e;
    --orange: #f39321;
    --white: #ffffff;
    --ink: #111111;
    --backdrop: #2a2a2a;
  }
  * { box-sizing: border-box; margin: 0; padding: 0; }
  html, body { width: 1200px; height: 942px; overflow: hidden; }
  body {
    background: var(--backdrop);
    position: relative;
    font-family: "Arimo", Arial, sans-serif;
  }
  .card {
    position: absolute;
    top: 321px;
    width: 520px;
    height: 300px;
    overflow: hidden;
  }

  /* Front */
  .card-front {
    left: 60px;
    background: var(--navy);
    color: var(--white);
  }
  .card-front .brand-name {
    position: absolute;
    left: 46px;
    top: 112px;
    font-family: "Noto Serif", Georgia, serif;
    font-size: 40px;
    color: var(--white);
    white-space: nowrap;
  }
  .card-front .web-address {
    position: absolute;
    left: 110px;
    top: 178px;
    font-family: "Arimo", Arial, sans-serif;
    font-size: 16px;
    letter-spacing: 1.6px;
    color: var(--white);
  }

  /* Back */
  .card-back {
    left: 620px;
    background: var(--white);
    color: var(--ink);
  }
  .header-strip {
    position: absolute;
    left: 0; top: 20px;
    width: 100%;
    height: 30px;
    background: var(--navy);
    display: flex;
    align-items: center;
    padding-left: 14px;
    gap: 16px;
  }
  .header-strip .brand-name {
    font-family: "Noto Serif", Georgia, serif;
    font-size: 14px;
    color: var(--white);
    white-space: nowrap;
  }
  .header-strip .web-box {
    background: var(--white);
    color: var(--ink);
    font-size: 13px;
    padding: 3px 8px;
    white-space: nowrap;
  }
  .person {
    position: absolute;
    left: 60px;
    top: 92px;
    font-size: 28px;
    color: var(--ink);
    white-space: nowrap;
  }
  .contacts {
    position: absolute;
    left: 100px;
    top: 146px;
    display: flex;
    flex-direction: column;
    gap: 10px;
  }
  .contact-line {
    display: flex;
    align-items: center;
    gap: 8px;
    font-size: 15px;
  }
  .contact-line.mobile { font-family: "Tinos", "Times New Roman", serif; font-size: 16px; }
  .contact-line svg { flex: none; }
  .footer-band {
    position: absolute;
    left: 0; bottom: 24px;
    width: 100%;
    height: 30px;
    background: var(--orange);
    display: flex;
    align-items: center;
    justify-content: space-between;
    padding: 0 26px;
    font-family: "Tinos", "Times New Roman", serif;
    font-size: 16px;
    color: var(--navy);
  }
</style>
</head>
<body>
  <section class="card card-front" aria-label="Business card front">
    <p class="brand-name">Harbourline Careers</p>
    <p class="web-address">www.harbourlinecareers.com.au</p>
  </section>

  <section class="card card-back" aria-label="Business card back">
    <div class="header-strip">
      <span class="brand-name">Harbourline Careers Australia</span>
      <span class="web-box">www.harbourlinecareers.com.au</span>
    </div>
    <p class="person">Gregory Palliser CEO</p>
    <div class="contacts">
      <p class="contact-line email">
        <svg width="22" height="16" viewBox="0 0 22 16" aria-hidden="true">
          <rect x="1" y="1" width="20" height="14" fill="none" stroke="#0b0f5e" stroke-width="2"/>
          <path d="M1 1 L11 9 L21 1" fill="none" stroke="#0b0f5e" stroke-width="2"/>
        </svg>
        gregory@harbourlinecareers.com.au
      </p>
      <p class="contact-line mobile">
        <svg width="22" height="20" viewBox="0 0 22 20" aria-hidden="true">
          <rect x="6" y="1" width="10" height="18" rx="2" fill="none" stroke="#0b0f5e" stroke-width="1.8"/>
          <rect x="8" y="4" width="6" height="7" fill="#0b0f5e"/>
        </svg>
        0412 937215
      </p>
    </div>
    <div class="footer-band">
      <span class="phone">Phone: 1300 574 816</span>
      <span class="fax">Fax: (03) 9172 4463</span>
    </div>
  </section>
</body>
</html>
```